Buch-/E-Book-Cover für Stille Pfade durch helle Tage
Zielgruppe
Das Buch 'Stille Pfade durch helle Tage' Untertitel: Gedanken und Bilder vom Wandern hinaus ins Weite' ist eine Community-Projekt und versammelt die Texte von 22 Coach*innen unter einem Cover. Die Rat gebenden Texte und sinnreichen Geschichten handeln von Mut, Selbstliebe, innerer Weisheit, persönlicher Entwicklung und natürlich vom Leben. Die Zielgruppe sind Frauen von 35-55 Jahren mit Interesse an Spiritualität, persönlicher Weiterentwicklung und Inspirationen. Sie wollen ihr Leben (um)gestalten und suchen nach neuen Möglichkeiten. Sie mögen warme und weiche Farben eher als allzu Schrilles, doch eher Modernes als Altbackenes oder Verschnörkeltes.
Aufgabenstellung
Es wäre schön, wenn der Geschenk-Charakter aus dem Titel auch im Cover widergespiegelt würde.

```html
<!DOCTYPE html>
<html lang="de">
<head>
<meta charset="utf-8">
<title>Stille Pfade durch helle Tage – Cover</title>
<link rel="stylesheet" href="https://fonts.googleapis.com/css2?family=Satisfy&family=Cormorant+Garamond:ital,wght@0,500;1,500;1,600&display=swap">
<style>
  :root {
    --paper: #f4f1ec;
    --sand: #efe1d0;
    --sage: #76a199;
    --rust: #a9493b;
    --photo-dark: #34493c;
    --photo-mid: #6f7d5f;
    --photo-warm: #c79c7e;
  }
  html, body {
    margin: 0;
    padding: 0;
    width: 848px;
    height: 1200px;
    overflow: hidden;
    background: var(--paper);
  }
  .cover {
    position: relative;
    width: 848px;
    height: 1200px;
    background: var(--paper);
    overflow: hidden;
  }
  .cover__shapes {
    position: absolute;
    inset: 0;
  }
  .cover__title {
    position: absolute;
    top: 48px;
    left: 0;
    width: 100%;
    margin: 0;
    text-align: center;
    font-family: "Satisfy", cursive;
    font-weight: 400;
    font-size: 96px;
    line-height: 108px;
    color: var(--sage);
  }
  .cover__title span { display: block; }
  .cover__subtitle {
    position: absolute;
    top: 392px;
    left: 0;
    width: 100%;
    margin: 0;
    text-align: center;
    font-family: "Cormorant Garamond", serif;
    font-weight: 500;
    font-size: 29px;
    line-height: 52px;
    letter-spacing: 3.5px;
    text-transform: uppercase;
    color: var(--rust);
  }
  .cover__subtitle span { display: block; }
  .cover__photo {
    position: absolute;
    left: 0;
    top: 0;
  }
  .cover__authors {
    position: absolute;
    top: 1072px;
    left: 0;
    width: 100%;
    margin: 0;
    text-align: center;
    font-family: "Cormorant Garamond", serif;
    font-style: italic;
    font-weight: 600;
    font-size: 25px;
    line-height: 35px;
    letter-spacing: 6px;
    color: var(--rust);
  }
  .cover__authors span { display: block; }
</style>
</head>
<body>
<main class="cover">
  <svg class="cover__shapes" width="848" height="1200" viewBox="0 0 848 1200" aria-hidden="true">
    <path fill="var(--sand)" d="M0 0 H470 C475 90 430 170 370 250 C300 340 280 400 260 470 C240 560 190 650 90 695 C55 710 25 715 0 722 Z"/>
    <path fill="var(--sand)" d="M848 715 C770 760 710 820 670 900 C640 960 640 1010 625 1060 C605 1120 605 1160 620 1200 H848 Z"/>
  </svg>

  <h1 class="cover__title">
    <span>Stille Pfade</span>
    <span>durch helle</span>
    <span>Tage</span>
  </h1>

  <p class="cover__subtitle">
    <span>Gedanken und Bilder</span>
    <span>vom Wandern hinaus ins Weite</span>
  </p>

  <svg class="cover__photo" width="848" height="1200" viewBox="0 0 848 1200" role="img" aria-label="Foto einer Frau mit geschlossenen Augen und einem Glas Tee vor grünen Blättern, in einer weichen Herzform">
    <defs>
      <linearGradient id="photoTone" x1="0" y1="0" x2="1" y2="0.6">
        <stop offset="0" stop-color="var(--photo-dark)"/>
        <stop offset="0.35" stop-color="var(--photo-warm)"/>
        <stop offset="0.6" stop-color="var(--photo-mid)"/>
        <stop offset="1" stop-color="var(--photo-dark)"/>
      </linearGradient>
    </defs>
    <path fill="url(#photoTone)" d="M200 494 C250 490 330 515 400 570 C450 530 520 520 590 535 C670 555 710 620 705 700 C700 790 640 860 560 905 C480 950 400 960 330 945 C260 930 210 880 180 810 C150 740 140 660 143 590 C146 530 165 497 200 494 Z"/>
  </svg>

  <p class="cover__authors">
    <span>Hier stehen ein oder zwei Unterzeile</span>
    <span>zu den Coach*innen</span>
  </p>
</main>
</body>
</html>
```